BrightFern Web Design Project

BrightFern IT solutions, a IT mananaged services company is looking to redesign current website (brightfernsolutions.example).

The website should convey professionalism within the managed it services community. The layout should invite users to explore other areas of the site. Should contain tools and other current information that clients or potential clients would find useful. Product pages, special offers and informational pages should be easily editable by non-programmers. Tidewarden.example is a good site to review as an example of the design components we like.

Target Market(s)

Professional services companies with 10-100 users

Industry/Entity Type

It Company

Requirements
Must have
• • Clickable icons and graphics are good
• SEO - Wordpress could be a great platform for us to work from as we already have internal experience with it and it’s easy to update. If not Wordpress, we would need something that is easy to SEO optimize
• An “our team” section with pictures
• Sell the message to potential clients why they need managed services
• Home page needs to convey our core services at a glance
• Home page needs to load quickly
• Screenshots of our monitoring and security reports
• Easy for us to update/edit certain areas
o New products
o Testimonials
Nice to have
• • Something like TW’s savings calculator - http://www.tidewarden.example/it-savings-calculator/
• Webform to enter service ticket requests
• Motion of home page banner
• Maybe pull in RSS feeds from current tech news sources
• Rotating content on all pages to keep it fresh
• “Fern-up” feature for monthly promos
Should not have
• • Should not be overly "techie" in feel.
• Not overly wordy (like current site)

```html
<!DOCTYPE html>
<html lang="en">
<head>
<meta charset="utf-8">
<title>BrightFern IT Solutions</title>
<link href="https://fonts.googleapis.com/css2?family=Questrial&family=Arimo:ital@0;1&display=swap" rel="stylesheet">
<style>
:root{
  --green-dark:#3c6b1e;
  --green:#6da32d;
  --green-light:#9cc94f;
  --green-text:#4a7a1f;
  --ink:#1a1a1a;
  --grey:#7a7a7a;
  --grey-light:#9a9a9a;
  --line:#d6d6d6;
  --panel-top:#ffffff;
  --panel-bottom:#e6e6e6;
  --bg:#ffffff;
}
*{box-sizing:border-box;margin:0;padding:0}
html,body{width:1200px;height:1139px;overflow:hidden;background:var(--bg)}
body{position:relative;font-family:"Arimo",Arial,sans-serif;color:var(--ink)}
.abs{position:absolute}
.brand{left:58px;top:18px;width:150px;text-align:center}
.brand-mark{width:70px;height:70px;border-radius:50%;background:radial-gradient(circle at 40% 35%,var(--green-light),var(--green-dark));margin:0 auto 10px}
.brand-name{font-family:"Questrial",sans-serif;font-size:30px;color:var(--green)}
.contact{right:44px;top:12px;text-align:right;font-family:"Questrial",sans-serif;letter-spacing:1px}
.contact .toll{font-size:22px;font-style:italic;color:var(--green-dark)}
.contact .toll b{color:var(--ink);font-weight:700}
.contact .phone{font-size:22px;font-style:italic;color:var(--green-dark);margin-top:10px}
.contact .phone span{color:var(--ink)}
.search{left:910px;top:103px;width:196px;height:27px;border:1px solid #c8c8c8;border-radius:3px;background:#fff}
.search svg{position:absolute;left:6px;top:6px}
.search-go{left:1117px;top:100px;width:41px;height:28px;border-radius:3px;background:linear-gradient(#9ed052,#5c9a22);color:#fff;font-size:17px;font-weight:700;text-align:center;line-height:28px;box-shadow:0 1px 2px rgba(0,0,0,.3)}
.main-nav{left:24px;top:169px;width:1150px;height:30px;border-radius:4px;background:linear-gradient(#a9d25f,#6ba229 55%,#4f8419);box-shadow:0 2px 3px rgba(0,0,0,.35);display:flex;align-items:center;justify-content:space-between;padding:0 48px 0 44px;font-size:14.5px;color:#fff}
.main-nav .current{color:#111}
.main-nav i{font-style:normal;color:#f0f6e4}
.tagline{left:34px;top:232px;font-family:"Questrial",sans-serif;font-size:30px;color:#8a8a8a;letter-spacing:.3px}
.banner{left:24px;top:278px;width:1150px;height:172px;background:linear-gradient(#fff 0%,#e9f4dc 30%,#74b43a 65%,#2f6a12 100%)}
.slider-dots{left:990px;top:419px;width:172px;height:20px;border-radius:4px;background:rgba(30,30,30,.85);display:flex;align-items:center;justify-content:center;gap:14px}
.slider-dots span{width:11px;height:11px;border-radius:50%;background:#c33}
.slider-dots span.on{background:#fff}
.intro-title{left:34px;top:476px;width:870px;font-family:"Questrial",sans-serif;font-size:22px;line-height:26px}
.intro-text{left:37px;top:542px;width:810px;font-size:14px;line-height:18px;color:var(--grey)}
.intro-text p+p{margin-top:18px}
.intro-more{left:778px;top:684px;font-size:13px;font-style:italic;color:var(--green-dark)}
.feature-art{left:902px;top:480px;width:268px;height:240px;border-radius:12px;background:radial-gradient(circle at 50% 40%,#7fb23a,#3f7a1b 60%,#fff 75%)}
.panel{top:732px;width:274px;height:292px;border:1px solid #dcdcdc;border-radius:6px;background:linear-gradient(var(--panel-top),var(--panel-bottom))}
.panel h2{position:absolute;left:15px;top:13px;font-family:"Questrial",sans-serif;font-weight:400;font-size:22px}
.panel .pic{position:absolute;left:10px;top:44px;width:254px;height:108px}
.panel .copy{position:absolute;left:15px;top:167px;width:245px;font-size:13.5px;line-height:17.5px;color:var(--grey)}
.panel .more{position:absolute;right:18px;bottom:10px;font-size:13px;font-style:italic;color:var(--green-dark)}
.products{list-style:none;position:absolute;left:16px;top:78px;width:240px}
.products li{font-size:14px;font-style:italic;border-bottom:1px solid var(--line);padding:4px 4px 8px}
.products li:last-child{border:0}
.quote{top:82px!important}
.client{position:absolute;right:8px;top:186px;font-size:13px;font-style:italic;color:var(--green-dark)}
.arrows{position:absolute;right:14px;bottom:14px}
.footer-bar{left:29px;top:1056px;width:1168px;height:36px;background:var(--green-dark);display:flex;align-items:center;color:#fff;font-size:13px}
.calc-icon{left:29px;top:1045px;width:50px;height:54px;border-radius:6px;background:linear-gradient(#eee,#bbb);border:1px solid #888}
.calc-label{position:absolute;left:56px;font-size:15px;font-style:italic}
.footer-nav{position:absolute;right:10px;display:flex;gap:0}
.footer-nav span{padding:0 16px;border-left:1px solid #cfe0bd}
.footer-nav span:first-child{border:0}
.copyright{left:34px;top:1109px;font-size:12px;font-style:italic;color:var(--grey-light)}
.copyright b{color:var(--green-dark)}
.social{left:1042px;top:1098px;display:flex;gap:12px}
.social span{width:34px;height:34px;border-radius:50%;background:radial-gradient(circle at 40% 35%,#7cc63c,#2e7110)}
</style>
</head>
<body>
<header>
  <div class="abs brand"><div class="brand-mark"></div><div class="brand-name">BrightFern</div></div>
  <div class="abs contact">
    <div class="toll">Toll Free: <b>(888) 555-0142</b></div>
    <div class="phone">Phone: <span>(480) 555-0173</span></div>
  </div>
  <div class="abs search"><svg width="14" height="14" viewBox="0 0 14 14"><circle cx="5.5" cy="5.5" r="4" fill="none" stroke="#333" stroke-width="2"/><line x1="8.5" y1="8.5" x2="13" y2="13" stroke="#333" stroke-width="2.4"/></svg></div>
  <div class="abs search-go">Go</div>
  <nav class="abs main-nav">
    <span class="current">Home</span><i>|</i><span>Solutions</span><i>|</i><span>About Us</span><i>|</i><span>IT Consulting</span><i>|</i><span>IT Programs</span><i>|</i><span>IT Security</span><i>|</i><span>Data Backup</span><i>|</i><span>Contact</span>
  </nav>
</header>
<main>
  <h1 class="abs tagline" style="font-weight:400">Nation's leading provider of computer network services and technology solutions</h1>
  <div class="abs banner" role="img" aria-label="Red apple resting in fresh green grass"></div>
  <div class="abs slider-dots"><span class="on"></span><span></span><span></span><span></span><span></span><span></span></div>
  <h2 class="abs intro-title" style="font-weight:400">BrightFern can help your business harness the power of new technology, making your business fast and efficient.</h2>
  <div class="abs intro-text">
    <p>In the information age of today, one must stay abreast of current technology in order to thrive. New advancements are made daily in dispersing information and collaborative computing. High-speed networks aid in the exchange of electronic information between businesses, their customers, vendors, and peers. Businesses that are quick to act and effectively implement this technology will rise to the top.</p>
    <p>Our specific service offerings including information technology planning, consulting, project management/implementation, data backup and recovery, security management, 24/7/365 remote monitoring and help desk assistance.</p>
  </div>
  <div class="abs intro-more">Read more...</div>
  <div class="abs feature-art" role="img" aria-label="Computer monitor covered in grass"></div>

  <section class="abs panel" style="left:32px">
    <h2>Our team</h2>
    <div class="pic" role="img" aria-label="Row of light bulbs growing from green leaves" style="background:linear-gradient(#f4f4f4,#dcdcdc 55%,#4f8a2a)"></div>
    <p class="copy">Lorem ipsum dolor sit amet, consectetuer adipiscing elit, sed diam nonummy nibh euismod tincidunt ut laoreet dolore magna aliquam erat volutpat.</p>
    <div class="more">Read more...</div>
  </section>
  <section class="abs panel" style="left:319px">
    <h2>Monitoring &amp; Security</h2>
    <div class="pic" role="img" aria-label="Globe circled by green recycling arrows" style="background:radial-gradient(circle at 50% 50%,#3a6fa0 0 28px,#5fae3a 29px 50px,transparent 51px)"></div>
    <p class="copy">Lorem ipsum dolor sit amet, consectetuer adipiscing elit, sed diam nonummy nibh euismod tincidunt ut laoreet dolore magna aliquam erat volutpat.</p>
    <div class="more">Read more...</div>
  </section>
  <section class="abs panel" style="left:605px">
    <h2>New Products</h2>
    <div role="img" aria-label="Seedling growing from coins" style="position:absolute;right:16px;top:10px;width:54px;height:40px;background:linear-gradient(#fff,#7bb33d 60%,#c9a94a)"></div>
    <ul class="products">
      <li>IT Assessment &amp; Strategic Planning</li>
      <li style="padding-top:14px">Infrastructure</li>
      <li style="padding-top:14px">Virtualization</li>
      <li style="padding-top:6px">Business Continuity Planning &amp; Disaster Recovery</li>
      <li style="padding-top:12px">Security</li>
    </ul>
  </section>
  <section class="abs panel" style="left:890px">
    <h2>Testimonials</h2>
    <svg style="position:absolute;right:12px;top:8px" width="56" height="50" viewBox="0 0 56 50"><path d="M4 4h48v30H22l-12 12V34H4z" fill="none" stroke="#4f8a2a" stroke-width="4" stroke-linejoin="round"/></svg>
    <p class="copy quote">Lorem ipsum dolor sit amet, consectetuer adipiscing elit, sed diam nonummy nibh euismod tincidunt ut laoreet dolore magna aliquam erat volutpat.</p>
    <div class="client">- Client one</div>
    <svg class="arrows" width="30" height="12" viewBox="0 0 30 12"><path d="M9 1L1 6l8 5z" fill="#999"/><path d="M21 1l8 5-8 5z" fill="#999"/></svg>
  </section>
</main>
<footer>
  <div class="abs footer-bar">
    <span class="calc-label">Calculate IT infrastructure</span>
    <nav class="footer-nav"><span>Home</span><span>Solutions</span><span>About Us</span><span>IT Consulting</span><span>IT Programs</span><span>IT Security</span><span>Data Backup</span><span>Contact</span></nav>
  </div>
  <div class="abs calc-icon" role="img" aria-label="Calculator icon"></div>
  <div class="abs copyright">© 2012 All copyrights reserved by <b>BrightFern</b> IT Solutions</div>
  <div class="abs social"><span></span><span></span><span></span></div>
</footer>
</body>
</html>
```